Postcard: Open Sky Circle

Text for front: HOW TO CHANGE THE WORLD IN ONE [note: the word "one" should be underlined] STEPHint: It's up to you...[Note: add arrow or something to indicate "turn over"]Text for back: You're going to spend your entire life with someone you can never get away from. (Guess who?) Wouldn't you rather that person #OpenSkyCircle than judgmental or critical? BE the change you want to see! Visit www.OpenSkyCircle-hub.example for daily Dawn Pebbles and community. PLEASE JOIN US![Note: add logo to left half of back side]Font preference for text: Josefin sans

Target Market(s)

People who would be attracted to Corvane church - teravian perennist message. It's spiritual without being overtly religious, so the target market is probably early 30s and up but ideally won't turn off Millennials (folks under 30). It should attract attention of people who are open-minded and committed to progressive social change, tired of an atmosphere of hate-mongering and divisiveness.

Requirements
Nice to have
• It would be nice to convey a sense of challenge - there is an idea of "dawn pebbles" so something related to fire/sparks is appropriate. This is meant to evoke a deeper, divine love more than a sense of romantic love. This love is more fierce than fluffy! Yet it calls us to be our best selves.
Should not have
• Please avoid excessive pink - just the logo is enough, as this design needs to appeal to men as well as women.

```html
<!DOCTYPE html>
<html lang="en">
<head>
<meta charset="utf-8">
<title>Open Sky Circle Postcard</title>
<link rel="stylesheet" href="https://fonts.googleapis.com/css2?family=Josefin+Sans:wght@400;600;700&family=Great+Vibes&display=swap">
<style>
  :root {
    --pink: #ec6f98;
    --pink-deep: #e0356a;
    --pink-soft: #f28cae;
    --sky: #a9daf6;
    --sky-deep: #6cc2ee;
    --frame: #d9323f;
    --tab: #322b29;
    --ink: #2a2322;
    --link: #4a8fd6;
    --paper: #ffffff;
    --outline: #6b6b6b;
  }
  * { margin: 0; padding: 0; box-sizing: border-box; }
  html, body { width: 1200px; height: 503px; overflow: hidden; background: var(--paper); }
  body { font-family: "Josefin Sans", sans-serif; }

  .sheet {
    position: relative; width: 1200px; height: 503px;
    border: 1.5px solid var(--outline); background: var(--paper);
  }
  .side-label {
    position: absolute; top: 42px; width: 200px; text-align: center;
    font-weight: 600; font-size: 34px; color: var(--ink); letter-spacing: 1px;
  }
  .side-label--front { left: 220px; }
  .side-label--back { left: 796px; }

  .card {
    position: absolute; top: 108px; width: 530px; height: 354px;
    border: 1.5px solid var(--frame); background: var(--paper);
  }
  .card--front { left: 45px; }
  .card--back { left: 632px; }
  .hang-tab {
    position: absolute; top: -1px; height: 32px; background: var(--tab);
  }
  .card--front .hang-tab { left: 221px; width: 72px; }
  .card--back .hang-tab { left: 220px; width: 88px; }

  /* Front headline */
  .headline { position: absolute; left: 0; width: 100%; text-align: center;
    color: var(--pink); font-weight: 600; line-height: 1; white-space: nowrap; }
  .headline--one { top: 52px; font-size: 56px; letter-spacing: 1px; }
  .headline--two { top: 104px; font-size: 84px; letter-spacing: 0; }
  .headline--three { top: 176px; font-size: 59px; letter-spacing: 0.5px; }

  .dot-o { position: relative; display: inline-block; }
  .dot-o::after {
    content: ""; position: absolute; left: 50%; top: 40%;
    width: 0.42em; height: 0.42em; border-radius: 50%;
    background: var(--sky); transform: translate(-50%, -50%);
  }
  .accent-one {
    color: var(--pink-deep); text-decoration: underline;
    text-decoration-thickness: 6px; text-underline-offset: 6px;
    margin: 0 0.12em;
  }
  .accent-one .dot-o::after { background: var(--sky-deep); }

  .hint {
    position: absolute; left: 30px; top: 262px;
    font-family: "Great Vibes", cursive; font-size: 38px; color: var(--pink);
  }
  .turn-arrow { position: absolute; left: 372px; top: 262px; width: 130px; height: 52px; }

  /* Back */
  .badge { position: absolute; left: 17px; top: 21px; width: 254px; height: 254px; }
  .badge-name {
    position: absolute; left: 17px; top: 21px; width: 254px; height: 254px;
    display: flex; align-items: center; justify-content: center; text-align: center;
    font-weight: 600; font-size: 30px; line-height: 1.15; color: var(--pink);
  }
  .message {
    position: absolute; left: 282px; top: 33px; width: 252px;
    text-align: center; font-size: 13.4px; line-height: 19.6px; color: var(--pink-deep);
    font-weight: 400;
  }
  .message a { color: var(--link); text-decoration: underline; }
  .join {
    position: absolute; left: 0; top: 271px; width: 100%; text-align: center;
    font-weight: 700; font-size: 53px; line-height: 1; color: var(--pink);
    letter-spacing: 0.5px;
  }
</style>
</head>
<body>
<main class="sheet">
  <h2 class="side-label side-label--front">FRONT</h2>
  <h2 class="side-label side-label--back">BACK</h2>

  <section class="card card--front" aria-label="Postcard front">
    <span class="hang-tab"></span>
    <h1>
      <span class="headline headline--one">H<span class="dot-o">O</span>W T<span class="dot-o">O</span> CHANGE</span>
      <span class="headline headline--two">THE W<span class="dot-o">O</span>RLD</span>
      <span class="headline headline--three">WITH<span class="accent-one"><span class="dot-o">O</span>NE</span>STEP</span>
    </h1>
    <p class="hint">Hint : Is up to you..</p>
    <svg class="turn-arrow" viewBox="0 0 130 52" aria-label="Turn over">
      <polygon points="0,0 130,26 24,26" fill="var(--pink-soft)"/>
      <polygon points="24,26 130,26 0,52" fill="var(--pink-deep)"/>
    </svg>
  </section>

  <section class="card card--back" aria-label="Postcard back">
    <span class="hang-tab"></span>
    <svg class="badge" viewBox="0 0 254 254" aria-hidden="true">
      <circle cx="127" cy="127" r="118" fill="none" stroke="var(--pink)" stroke-width="17"/>
    </svg>
    <div class="badge-name">Open Sky<br>Circle</div>
    <p class="message">
      You're going to spend<br>
      your entire life with<br>
      someone you can never<br>
      get away from.<br>
      (Guess who?)<br>
      Wouldn't you rather that<br>
      person #OpenSkyCircle<br>
      than judgmental or critical?<br>
      BE the change you want to see!<br>
      Visit <a href="#">www.OpenSkyCircle-hub.example</a><br>
      for daily Dawn Pebbles and community.
    </p>
    <p class="join">PLEASE J<span class="dot-o">O</span>IN US!</p>
  </section>
</main>
</body>
</html>
```